Business card for Eyelash extension salon in Beverly Hills,California USA

We need new business card for our salon in Beverly Hills. The salon name is 'Lumarra' . We would like to have...Business name: Lumarra Name of person: will provide later Address 6128 N.Corbel Ridge Blvd Beverly Hills , CA 90210 Phone: will provide later (Text only) Web: www.lumarrastudio-example.com Pictogrid icon, Friendvale icon follow us for seasonal campaign and news @lumarrastudioexample Design should look elegant, high-end, clean, simple, cohesive with my brand. Please refer my brand board. Business name color will be metallic bronzy color. Im thinking grey background or white background. Thanks

Target Market(s)

25-35. Gender neutral. People who are in Entertainment business industry.
This is High-end Eyelash extension salon in Beverly Hills

Industry/Entity Type

Beauty Salon

Contact Information for Business Card

Business name: Lumarra
Name of person: will provide later
Address 6128 N.Corbel Ridge Blvd Beverly Hills , CA 90210
Phone: will provide later (Text only)
Web: www.lumarrastudio-example.com
Pictogrid icon, Friendvale icon
follow us for seasonal campaign and news @lumarrastudioexample

Requirements
Must have
• Beautiful, elegant, clean and simple look but very attractive and modern
Should not have
• We don't like too clutter, too busy designs.

```html
<!DOCTYPE html>
<html lang="en">
<head>
<meta charset="utf-8">
<title>Lumarra Beverly Hills – Business Card</title>
<link rel="stylesheet" href="https://fonts.googleapis.com/css2?family=Libre+Baskerville:wght@400;700&family=Montserrat:wght@400;500&display=swap">
<style>
  :root {
    --backdrop: #1f1f1f;
    --bronze: #8a6446;
    --bronze-deep: #7a563b;
    --bronze-light: #b08866;
    --tan: #c9a88a;
    --paper: #fbfaf8;
    --ink: #3b2f27;
    --rule: #d9b9a2;
    --serif: "Libre Baskerville", Georgia, serif;
    --sans: "Montserrat", Arial, sans-serif;
  }
  * { box-sizing: border-box; margin: 0; padding: 0; }
  html, body { width: 1200px; height: 800px; overflow: hidden; }
  body { background: var(--backdrop); position: relative; font-family: var(--serif); }

  .card {
    position: absolute;
    width: 560px;
    height: 320px;
    border-radius: 3px;
    overflow: hidden;
    box-shadow: 0 14px 30px rgba(0,0,0,.45);
  }

  /* Front */
  .card-front { left: 150px; top: 70px; background: var(--bronze); }
  .lash-pattern {
    position: absolute; inset: 0;
    background: radial-gradient(ellipse at center, #91694b 0%, var(--bronze) 70%);
  }
  .front-logo {
    position: absolute; left: 0; right: 0; top: 118px;
    text-align: center; color: #ffffff;
  }
  .front-logo .brand-name {
    font-family: var(--serif); font-weight: 400;
    font-size: 58px; letter-spacing: 1px; line-height: 1;
  }
  .front-logo .brand-place {
    display: block; margin-top: 10px;
    font-family: var(--sans); font-size: 9px; letter-spacing: 3px;
    padding-left: 170px;
  }

  /* Back */
  .card-back { left: 490px; top: 410px; background: var(--paper); }
  .back-logo {
    position: absolute; right: 70px; top: 42px; text-align: right; color: var(--bronze);
  }
  .back-logo .brand-name {
    font-family: var(--serif); font-weight: 400; font-size: 38px; line-height: 1;
  }
  .back-logo .brand-place {
    display: block; margin-top: 6px;
    font-family: var(--sans); font-size: 6px; letter-spacing: 2px; color: var(--bronze-light);
  }
  .rule-top {
    position: absolute; left: 0; right: 0; top: 126px; height: 1px; background: var(--rule);
  }
  .social-list {
    position: absolute; right: 56px; top: 136px; display: flex; gap: 10px;
    list-style: none;
  }
  .social-item {
    display: flex; align-items: center; gap: 4px;
    font-family: var(--serif); font-size: 9px; color: var(--bronze);
  }
  .social-item::before {
    content: ""; width: 14px; height: 14px; border: 1.2px solid var(--bronze); border-radius: 50%;
  }
  .person-name {
    position: absolute; left: 36px; top: 162px;
    font-family: var(--serif); font-weight: 700; font-size: 19px; letter-spacing: 1.5px;
    color: var(--bronze);
  }
  .rule-name {
    position: absolute; left: 0; width: 330px; top: 192px; height: 1px; background: var(--rule);
  }
  .band-handle {
    position: absolute; right: 0; top: 178px; width: 300px; height: 22px;
    background: var(--bronze); color: #fff;
    font-family: var(--serif); font-size: 11.5px; letter-spacing: .8px;
    display: flex; align-items: center; justify-content: flex-end; padding-right: 16px;
  }
  .band-step {
    position: absolute; left: 190px; top: 200px; width: 370px; height: 88px;
    background: var(--tan);
    clip-path: polygon(58% 0, 100% 0, 100% 0, 14% 100%, 0 100%, 0 100%, 50% 0);
    clip-path: polygon(50% 0, 62% 0, 10% 100%, -2% 100%);
    opacity: .75;
  }
  .contact-list {
    position: absolute; left: 36px; top: 206px; list-style: none;
    font-family: var(--serif); font-size: 11.5px; color: var(--ink);
  }
  .contact-list li { display: flex; align-items: center; gap: 10px; height: 20px; }
  .contact-list svg { width: 11px; height: 11px; fill: var(--bronze-deep); flex: none; }
  .band-follow {
    position: absolute; left: 0; right: 0; bottom: 0; height: 32px;
    background: var(--bronze); color: #fff;
    font-family: var(--serif); font-size: 12.5px; letter-spacing: 1.2px;
    display: flex; align-items: center; padding-left: 36px;
  }
</style>
</head>
<body>

  <section class="card card-front" aria-label="Card front">
    <div class="lash-pattern" role="img" aria-label="Faint repeating pattern of closed eyelashes in darker bronze"></div>
    <div class="front-logo">
      <div class="brand-name">Lumarra</div>
      <span class="brand-place">BEVERLY HILLS</span>
    </div>
  </section>

  <section class="card card-back" aria-label="Card back">
    <div class="back-logo">
      <div class="brand-name">Lumarra</div>
      <span class="brand-place">BEVERLY HILLS</span>
    </div>
    <div class="rule-top"></div>
    <ul class="social-list">
      <li class="social-item">Pictogrid</li>
      <li class="social-item">Friendvale</li>
    </ul>

    <h1 class="person-name">Your Name</h1>
    <div class="rule-name"></div>

    <div class="band-step"></div>
    <div class="band-handle">@lumarrastudioexample</div>

    <ul class="contact-list">
      <li>
        <svg viewBox="0 0 24 24" aria-hidden="true"><path d="M6.6 10.8a15.1 15.1 0 0 0 6.6 6.6l2.2-2.2a1 1 0 0 1 1-.25 11.4 11.4 0 0 0 3.6.57 1 1 0 0 1 1 1V20a1 1 0 0 1-1 1A17 17 0 0 1 3 4a1 1 0 0 1 1-1h3.5a1 1 0 0 1 1 1c0 1.25.2 2.45.57 3.57a1 1 0 0 1-.25 1z"/></svg>
        Your Contact Number
      </li>
      <li>
        <svg viewBox="0 0 24 24" aria-hidden="true"><path d="M12 2a10 10 0 1 0 0 20 10 10 0 0 0 0-20zm6.9 6h-2.9a15.6 15.6 0 0 0-1.4-3.6A8 8 0 0 1 18.9 8zM12 4c.8 1.2 1.5 2.5 1.9 4h-3.8c.4-1.5 1.1-2.8 1.9-4zM4.3 14a8 8 0 0 1 0-4h3.4a16.5 16.5 0 0 0 0 4zm.8 2h2.9c.3 1.3.8 2.5 1.4 3.6A8 8 0 0 1 5.1 16zM8 8H5.1a8 8 0 0 1 4.3-3.6C8.8 5.5 8.3 6.7 8 8zm4 12c-.8-1.2-1.5-2.5-1.9-4h3.8c-.4 1.5-1.1 2.8-1.9 4zm2.3-6H9.7a14.7 14.7 0 0 1 0-4h4.6a14.7 14.7 0 0 1 0 4zm.3 5.6c.6-1.1 1.1-2.3 1.4-3.6h2.9a8 8 0 0 1-4.3 3.6zm1.7-5.6a16.5 16.5 0 0 0 0-4h3.4a8 8 0 0 1 0 4z"/></svg>
        www.lumarrastudio-example.com
      </li>
      <li>
        <svg viewBox="0 0 24 24" aria-hidden="true"><path d="M12 2a7 7 0 0 0-7 7c0 5.2 7 13 7 13s7-7.8 7-13a7 7 0 0 0-7-7zm0 9.5A2.5 2.5 0 1 1 12 6.5a2.5 2.5 0 0 1 0 5z"/></svg>
        6128 N.Corbel Ridge Blvd Beverly Hills , CA 90210
      </li>
    </ul>

    <div class="band-follow">follow us for seasonal campaign and news</div>
  </section>

</body>
</html>
```